Restaurant Business Card Template

I need a business card created in the same color scheme and style as the attached label. Preferably it'd be in a .ai format.

Industry/Entity Type

German Restaurant

Contact Information for Business Card

Dorine Pekko, Front of House Manager, 612.307.4419, dorine@brunhofstuberestaurant.example, info@brunhofstuberestaurant.example, 417 Tamble Ave., Lower Level, Keldorn Falls, KF 98751.

Requirements
Must have
• Matching fonts and colors.
Nice to have
• If not able to match secondary font, something similar.

```html
<!DOCTYPE html>
<html lang="en">
<head>
<meta charset="utf-8">
<title>Brunhof Stube Restaurant – Business Card</title>
<link rel="stylesheet" href="https://fonts.googleapis.com/css2?family=Alfa+Slab+One&family=Pathway+Gothic+One&display=swap">
<style>
  :root {
    --backdrop: #d8d3c8;
    --paper: #f3efe4;
    --paper-warm: #e9e1cc;
    --ink: #1e1c1a;
    --bavarian-blue: #7fa6c4;
    --bavarian-cream: #e6d8b2;
    --slate: #8ea2aa;
    --slate-deep: #7b9199;
  }
  * { margin: 0; padding: 0; box-sizing: border-box; }
  html, body {
    width: 1200px;
    height: 780px;
    overflow: hidden;
    background: var(--backdrop);
  }
  .card {
    position: absolute;
    left: 75px;
    top: 90px;
    width: 1050px;
    height: 600px;
    background: radial-gradient(ellipse at 60% 40%, var(--paper) 0%, var(--paper) 45%, var(--paper-warm) 100%);
    box-shadow: 0 10px 30px rgba(0,0,0,0.25);
    overflow: hidden;
    font-family: "Pathway Gothic One", sans-serif;
    color: var(--ink);
  }
  .diamond-field {
    position: absolute;
    left: 0;
    top: 0;
    width: 620px;
    height: 600px;
  }
  .brush-edge {
    position: absolute;
    left: 440px;
    top: 300px;
    width: 610px;
    height: 300px;
  }
  .brand {
    position: absolute;
    left: 70px;
    top: 220px;
    width: 340px;
    display: flex;
    align-items: center;
    gap: 14px;
  }
  .brand-dot {
    flex: none;
    width: 46px;
    height: 46px;
    border-radius: 50%;
    background: var(--ink);
  }
  .brand-name {
    font-size: 44px;
    line-height: 1.05;
    color: var(--ink);
    letter-spacing: 0.5px;
  }
  .person {
    position: absolute;
    left: 470px;
    top: 70px;
  }
  .person-name {
    font-family: "Alfa Slab One", serif;
    font-size: 50px;
    letter-spacing: 2px;
    line-height: 1;
  }
  .person-role {
    font-size: 30px;
    font-style: italic;
    margin-top: 6px;
  }
  .contact {
    position: absolute;
    left: 530px;
    top: 205px;
    list-style: none;
    font-size: 28px;
    line-height: 40px;
  }
  .contact li {
    display: flex;
    align-items: center;
    gap: 14px;
  }
  .contact svg { width: 20px; height: 20px; flex: none; }
  .address {
    position: absolute;
    left: 596px;
    top: 345px;
    font-size: 30px;
    line-height: 40px;
    font-style: normal;
  }
</style>
</head>
<body>
  <section class="card">
    <svg class="diamond-field" role="img" aria-label="Faded blue and cream Bavarian diamond pattern along the top-left of the card" viewBox="0 0 620 600">
      <defs>
        <linearGradient id="diamondFade" x1="0" y1="1" x2="1" y2="0">
          <stop offset="0" stop-color="var(--bavarian-blue)" stop-opacity="0.85"/>
          <stop offset="0.45" stop-color="var(--bavarian-cream)" stop-opacity="0.7"/>
          <stop offset="1" stop-color="var(--bavarian-cream)" stop-opacity="0"/>
        </linearGradient>
        <linearGradient id="diamondDown" x1="0" y1="0" x2="0" y2="1">
          <stop offset="0" stop-color="#fff" stop-opacity="1"/>
          <stop offset="0.7" stop-color="#fff" stop-opacity="0.6"/>
          <stop offset="1" stop-color="#fff" stop-opacity="0"/>
        </linearGradient>
        <mask id="diamondMask">
          <rect width="620" height="600" fill="url(#diamondDown)"/>
        </mask>
      </defs>
      <rect width="620" height="600" fill="url(#diamondFade)" mask="url(#diamondMask)"/>
    </svg>

    <svg class="brush-edge" role="img" aria-label="Rough slate-blue brush stroke along the lower right edge" viewBox="0 0 610 300" preserveAspectRatio="none">
      <defs>
        <linearGradient id="brushTone" x1="0" y1="1" x2="1" y2="0">
          <stop offset="0" stop-color="var(--slate)" stop-opacity="0.55"/>
          <stop offset="1" stop-color="var(--slate-deep)" stop-opacity="0.95"/>
        </linearGradient>
      </defs>
      <path d="M0 300 C120 290 200 250 300 220 C380 195 420 150 470 110 C520 70 560 30 610 0 L610 300 Z" fill="url(#brushTone)"/>
    </svg>

    <div class="brand">
      <span class="brand-dot"></span>
      <span class="brand-name">Brunhof Stube Restaurant</span>
    </div>

    <header class="person">
      <h1 class="person-name">Dorine Pekko</h1>
      <p class="person-role">Front of House Manager</p>
    </header>

    <ul class="contact">
      <li>
        <svg viewBox="0 0 20 20" aria-hidden="true"><path d="M5 2 L8 2 L9 6 L7 8 C8 11 9 12 12 13 L14 11 L18 12 L18 15 C18 17 16 18 14 18 C8 17 3 12 2 6 C2 4 3 2 5 2 Z" fill="var(--ink)"/></svg>
        <span>612.307.4419</span>
      </li>
      <li>
        <svg viewBox="0 0 20 20" aria-hidden="true"><rect x="2" y="4" width="16" height="12" fill="var(--ink)"/><path d="M2 4 L10 11 L18 4" stroke="var(--paper)" stroke-width="1.5" fill="none"/></svg>
        <span>dorine@brunhofstuberestaurant.example</span>
      </li>
      <li>
        <svg viewBox="0 0 20 20" aria-hidden="true"><rect x="2" y="4" width="16" height="12" fill="var(--ink)"/><path d="M2 4 L10 11 L18 4" stroke="var(--paper)" stroke-width="1.5" fill="none"/></svg>
        <span>info@brunhofstuberestaurant.example</span>
      </li>
    </ul>

    <address class="address">
      417 Tamble Ave., Lower Level<br>
      Keldorn Falls, KF 98751
    </address>
  </section>
</body>
</html>
```